Business Card Design Project

New business cards that encompass our new logo.
Looking for -
Name, Title, Cell Phone, Email, Address (2 lines), Main Phone, Fax, and website.
Reason: I don't like the graphics used to show phone, fax, cell, email, web, and address.....
I like the double sided cards with logo's on the back. I do not like the logos for phone, fax, cell, address, email, or web.

```html
<!DOCTYPE html>
<html lang="en">
<head>
<meta charset="utf-8">
<title>Northfield Kitchen Supply – Business Cards</title>
<link href="https://fonts.googleapis.com/css2?family=Montserrat:wght@400;500;600;700;800&display=swap" rel="stylesheet">
<style>
  :root {
    --backdrop: #e4e5e8;
    --card-white: #f7f7f7;
    --brand-blue: #1b3f7f;
    --text-dark: #1d1d1f;
    --text-mid: #3b3b3e;
    --text-grey: #8a8a8e;
    --band-text: #ffffff;
  }
  * { margin: 0; padding: 0; box-sizing: border-box; }
  html, body {
    width: 1200px; height: 1000px; overflow: hidden;
    background: var(--backdrop);
    font-family: "Montserrat", sans-serif;
  }
  .canvas { position: relative; width: 1200px; height: 1000px; }
  .card {
    position: absolute; left: 180px;
    width: 840px; height: 480px;
    background: var(--card-white);
    overflow: hidden;
    box-shadow: 0 10px 28px rgba(0,0,0,.18);
  }
  .card--front { top: 14px; }
  .card--back { top: 506px; }
  .card__band { position: absolute; inset: 0; width: 840px; height: 480px; }
  .wordmark {
    position: absolute;
    color: var(--brand-blue);
    font-weight: 800;
    letter-spacing: 1px;
    line-height: 1.05;
    display: flex; align-items: center; gap: 14px;
  }
  .wordmark__square { width: 34px; height: 34px; background: var(--brand-blue); flex: none; }
  .wordmark__name { font-size: 40px; }
  .wordmark__name small { display: block; font-size: 19px; letter-spacing: 3px; font-weight: 800; }
  .card--front .wordmark { left: 150px; top: 150px; }
  .card--back .wordmark { left: 46px; top: 340px; }
  .website-band {
    position: absolute; right: 46px; top: 236px;
    color: var(--band-text); font-size: 21px; font-weight: 500; letter-spacing: 1px;
    transform: rotate(-8deg); transform-origin: right center;
  }
  .holder {
    position: absolute; right: 40px; top: 28px; text-align: right; color: var(--band-text);
    line-height: 1.2;
    transform: rotate(-6deg); transform-origin: right top;
  }
  .holder__name { font-size: 25px; font-weight: 700; letter-spacing: 1.5px; }
  .holder__title { font-size: 17px; font-weight: 400; letter-spacing: 1px; }
  .divider {
    position: absolute; left: 420px; top: 282px; width: 2px; height: 170px;
    background: linear-gradient(var(--brand-blue), rgba(27,63,127,0));
  }
  .contact { position: absolute; left: 448px; top: 272px; color: var(--text-dark); }
  .contact__address { font-size: 18px; font-weight: 500; letter-spacing: .8px; line-height: 1.3; margin-bottom: 8px; color: var(--text-mid); }
  .contact__list { display: grid; grid-template-columns: 100px auto; row-gap: 2px; font-size: 18px; letter-spacing: .6px; }
  .contact__list dt { color: var(--text-grey); font-weight: 500; }
  .contact__list dd { font-weight: 600; }
</style>
</head>
<body>
<main class="canvas">

  <section class="card card--front" aria-label="Card front">
    <svg class="card__band" viewBox="0 0 840 480" aria-hidden="true">
      <path d="M0 340 C 260 300, 560 210, 840 110 L 840 300 C 560 380, 300 440, 0 480 Z" fill="var(--brand-blue)"/>
    </svg>
    <div class="wordmark">
      <span class="wordmark__square"></span>
      <span class="wordmark__name">NORTHFIELD<small>KITCHEN SUPPLY</small></span>
    </div>
    <p class="website-band">www.Yourweb.com</p>
  </section>

  <section class="card card--back" aria-label="Card back">
    <svg class="card__band" viewBox="0 0 840 480" aria-hidden="true">
      <path d="M0 0 L 840 0 L 840 130 C 560 200, 260 260, 0 300 Z" fill="var(--brand-blue)"/>
    </svg>
    <div class="holder">
      <p class="holder__name">YOUR NAME</p>
      <p class="holder__title">Owner</p>
    </div>
    <div class="wordmark">
      <span class="wordmark__square"></span>
      <span class="wordmark__name">NORTHFIELD<small>KITCHEN SUPPLY</small></span>
    </div>
    <div class="divider"></div>
    <div class="contact">
      <p class="contact__address">PO BOX 1500, Your city<br>CA 2000</p>
      <dl class="contact__list">
        <dt>Tel</dt><dd>:123-456-789</dd>
        <dt>Fax</dt><dd>:123-456-789</dd>
        <dt>Mobile</dt><dd>:123-456-789</dd>
        <dt>Email</dt><dd>:admin@northfieldks.com</dd>
        <dt>Web</dt><dd>:www.Yourweb.com</dd>
      </dl>
    </div>
  </section>

</main>
</body>
</html>
```